Company Website

We need an interactive website designed that for new company. Our company is in the Automotive fleet maintenance business. We have wide ranging customers in many industries e.g Aviation industry, construction industry, transportation etc.
We would like the website to have login accounts where customers can register, login and access their service history. Also we would like to have an appointment system where customers could schedule appointments, once appointments are made that time would no longer be available to be selected as it would be booked etc.

The website should also be updatable and provide areas for showcasing
Our services
Products/parts (possibly store front)
Customer feedback
Appointments
Our customers (where our customers can advertise or be showcased)
About us
Contacts
gallery

We would like designs that have a modern, corporate feel, One that is user friendly.
prefer a design that does not look like a template.

Target Market(s)

Medium to large companies, small business owners and the general motoring public.

Industry/Entity Type

Construction

Requirements
Must have
• Customer login set up so a database of customer vehicle maintenance history as well as the ability to schedule repairs via their account. They could also check the status of a repair.
Nice to have
• Photo gallery to show case current projects.
Our customers page where we can show case our clients they could also post their events on there, promotions etc.

The theme Should be something that's reflective of our core business; fleet maintenance. It would be nice to capture some sort of background in there that depicts some of that for example mixer trucks, tractors,loaders excavators forklifts cars trucks. That's what we deal with. It's up to the designer to capture the Essence of this as much as possible. Impress me.
Should not have
• Would prefer a custom website not a template.

```html
<!DOCTYPE html>
<html lang="en">
<head>
<meta charset="utf-8">
<title>Keystone Fleet &amp; Auto Maintenance</title>
<link href="https://fonts.googleapis.com/css2?family=Arimo:wght@400;700&family=Roboto+Condensed:wght@400&display=swap" rel="stylesheet">
<style>
:root{
  --red:#c8161d;
  --red-light:#e84a4f;
  --red-dark:#b51218;
  --ink:#3a3a3a;
  --muted:#666;
  --line:#c9c9c9;
  --navy:#1d3f80;
  --footer:#4b4b4b;
  --white:#fff;
}
*{margin:0;padding:0;box-sizing:border-box}
html,body{width:794px;height:1200px;overflow:hidden;background:var(--white)}
body{position:relative;font-family:"Arimo",Arial,sans-serif;color:var(--ink)}
.abs{position:absolute}
.brand{left:94px;top:22px;color:var(--red);font-weight:700;font-size:19px;letter-spacing:.5px;display:flex;align-items:center;gap:7px}
.brand-mark{width:14px;height:14px;background:var(--red);border-radius:50%}
.brand-sub{left:115px;top:48px;color:var(--red);font-weight:700;font-size:8px}
.search{left:580px;top:46px;width:118px;height:20px;border:1px solid #bdbdbd;border-radius:5px;background:linear-gradient(#fafafa,#e2e2e2);font-size:8px;color:#888;padding:5px 7px}
.search svg{position:absolute;right:6px;top:4px}
.nav{left:93px;top:82px;width:608px;height:36px;background:linear-gradient(var(--red-light),var(--red-dark));display:flex;align-items:center;padding-left:29px;gap:0}
.nav a{color:var(--white);font-size:8.5px;text-decoration:none;margin-right:26.5px}
.hero{left:93px;top:118px;width:608px;height:270px;background:linear-gradient(180deg,#7fa6d6 0%,#c9d9ee 55%,#9a9a9a 75%,#6e6e6e 100%)}
.hero-title{left:502px;top:194px;font-family:"Roboto Condensed",Arial,sans-serif;font-size:22px;line-height:28px}
.hero-title .a{color:var(--red)}
.hero-title .b{color:#111;font-size:25px}
.dots{left:651px;top:368px;display:flex;gap:4px}
.dots i{width:8px;height:8px;border-radius:50%;background:var(--white)}
.dots i:first-child{background:var(--red)}
h2{font-weight:400;color:var(--red);font-size:13px}
.welcome{left:93px;top:404px;width:608px;text-align:center}
.welcome p{font-size:7.3px;color:var(--muted);line-height:16px;margin-top:8px;padding:0 38px}
.card-img{top:518px;width:188px;height:134px}
.card h3{font-weight:400;color:var(--red);font-size:13px;line-height:14px}
.card p{font-size:7px;color:var(--muted);line-height:15px;margin-top:6px;width:186px}
.btn{height:21px;border:1px solid #b9b9b9;border-radius:4px;background:linear-gradient(#fdfdfd,#dcdcdc);font-size:7.5px;color:#555;display:flex;align-items:center;justify-content:center;box-shadow:0 1px 1px rgba(0,0,0,.2)}
.about-text{left:254px;top:800px;width:228px;font-size:7.6px;line-height:16.8px;color:var(--muted)}
.signin{left:497px;top:801px;width:202px;height:149px;border:1px solid var(--line)}
.signin h2{text-align:center;margin-top:10px}
.field{left:22px;width:156px;height:22px;border:1px solid #bbb;border-radius:4px;background:linear-gradient(#fafafa,#e0e0e0);font-size:7.5px;color:#666;padding:6px 9px}
.gallery{left:93px;top:979px;width:608px;height:143px;background:var(--navy)}
.thumb{top:33px;width:124px;height:80px}
.footer{left:0;top:1137px;width:794px;height:63px;background:var(--footer);color:var(--white)}
.flinks{left:95px;top:18px;display:flex;font-size:7.3px}
.flinks span{margin-right:10px}
.copy{left:95px;top:37px;font-size:7.3px}
.follow{left:585px;top:28px;font-size:7.3px;display:flex;align-items:center;gap:5px}
.follow i{width:14px;height:14px;border-radius:50%;background:#6d6d6d;display:inline-block}
</style>
</head>
<body>

<div class="abs brand"><span class="brand-mark"></span>KEYSTONE</div>
<div class="abs brand-sub">FLEET &amp; AUTO MAINTENANCE</div>
<div class="abs search">Search
  <svg width="12" height="12" viewBox="0 0 12 12"><circle cx="7" cy="5" r="3.5" fill="none" stroke="#888" stroke-width="1.3"/><line x1="4.5" y1="7.5" x2="1.5" y2="10.5" stroke="#888" stroke-width="1.6"/></svg>
</div>

<nav class="abs nav">
  <a>Home</a><a>Our services</a><a>Products</a><a>Feedback</a><a>Appointments</a><a>Customers</a><a>About us</a><a>Contacts</a><a>Gallery</a>
</nav>

<div class="abs hero" role="img" aria-label="White cement mixer truck parked under a blue cloudy sky"></div>
<div class="abs hero-title"><div class="a">Keystone Fleet</div><div class="b">Auto Maintenance</div></div>
<div class="abs dots"><i></i><i></i><i></i></div>

<section class="abs welcome">
  <h2>Welcome to construction</h2>
  <p>Contrary to popular belief, Lorem Ipsum is not simply random text. It has roots in a piece of classical Latin literature from 45 BC, making it over 2000 years old. Daniel Harlow, a Latin professor at Westbrook College in Virginia, looked up one of the more obscure Latin words, consectetur, from a Lorem Ipsum passage, and going through the cites of the word in classical literature, discovered the undoubtable source.</p>
</section>

<h2 class="abs" style="left:93px;top:490px">Feature our projects</h2>

<div class="abs card-img" style="left:93px;background:linear-gradient(#b9cde0,#c23a35 55%,#777)" role="img" aria-label="Red cement mixer truck"></div>
<div class="abs card-img" style="left:303px;background:linear-gradient(#c7d8ea,#b22a2a 50%,#3f5a2a)" role="img" aria-label="Red farm tractor on grass"></div>
<div class="abs card-img" style="left:512px;background:linear-gradient(#8fb3dc,#e2b524 50%,#a0603a)" role="img" aria-label="Yellow excavator on a dirt site"></div>

<div class="abs card" style="left:93px;top:662px">
  <h3>Mixer trucks</h3>
  <p>Lorem Ipsum is simply dummy text of the printing and typesetting industry. Lorem Ipsum has been the industry's standard dummy text ever since ...</p>
</div>
<div class="abs card" style="left:303px;top:662px">
  <h3>Tractors</h3>
  <p>Lorem Ipsum is simply dummy text of the printing and typesetting industry. Lorem Ipsum has been the industry's standard dummy text ever since ...</p>
</div>
<div class="abs card" style="left:513px;top:662px">
  <h3>Loaders excavators forklifts<br>cars trucks.</h3>
  <p>Lorem Ipsum is simply dummy text of the printing and typesetting industry. Lorem Ipsum ...</p>
</div>

<div class="abs btn" style="left:93px;top:737px;width:68px">View More</div>
<div class="abs btn" style="left:304px;top:737px;width:68px">View More</div>
<div class="abs btn" style="left:513px;top:737px;width:68px">View More</div>

<h2 class="abs" style="left:93px;top:774px">About us</h2>
<div class="abs" style="left:93px;top:802px;width:147px;height:128px;background:linear-gradient(#dcdcdc,#b7a597 60%,#2b2e45)" role="img" aria-label="Portrait of the company director"></div>
<p class="abs about-text">Contrary to popular belief, Lorem Ipsum is not simply random text. It has roots in a piece of classical Latin literature from 45 BC, making it over 2000 years old. Daniel Harlow, a Latin professor at Westbrook College in Virginia, looked up one of the in discovered the undoubtable source...</p>
<div class="abs btn" style="left:252px;top:908px;width:114px">Click more info</div>

<div class="abs signin">
  <h2>Sign in to your account</h2>
  <div class="abs field" style="top:36px">User name :</div>
  <div class="abs field" style="top:68px">Pass word :</div>
  <div class="abs btn" style="left:119px;top:104px;width:60px;height:24px;font-size:9px">Login</div>
</div>

<h2 class="abs" style="left:93px;top:954px">Photo gallery</h2>
<div class="abs gallery">
  <svg class="abs" style="left:6px;top:63px" width="10" height="18" viewBox="0 0 10 18"><polyline points="8,1 2,9 8,17" fill="none" stroke="#fff" stroke-width="1.5"/></svg>
  <div class="abs thumb" style="left:26px;background:linear-gradient(#fff,#6aa33a 60%,#e0d23a)" role="img" aria-label="Toy tractor with front loader"></div>
  <div class="abs thumb" style="left:170px;background:linear-gradient(#4a86c8,#cfe1f2 55%,#6ea0d8)" role="img" aria-label="Passenger airliner in flight"></div>
  <div class="abs thumb" style="left:315px;background:linear-gradient(#bfc6cc,#e8e8e8 50%,#5a5a5a)" role="img" aria-label="White cement mixer truck"></div>
  <div class="abs thumb" style="left:457px;background:linear-gradient(#8fbce0,#d9a12a 50%,#4c7a2e)" role="img" aria-label="Orange tractor in a field"></div>
  <svg class="abs" style="left:592px;top:63px" width="10" height="18" viewBox="0 0 10 18"><polyline points="2,1 8,9 2,17" fill="none" stroke="#fff" stroke-width="1.5"/></svg>
</div>

<footer class="abs footer">
  <div class="abs flinks"><span>Home</span><span>Our services</span><span>Products</span><span>Feedback</span><span>Appointments</span><span>Customers</span><span>About us</span><span>Contacts</span><span>Gallery</span></div>
  <div class="abs copy">Copyright 2013 Keystone Fleet &amp; Auto Maintenance.All Right Reserved.</div>
  <div class="abs follow">Follow us :&nbsp;&nbsp;<i></i><i></i><i></i><i></i></div>
</footer>

</body>
</html>
```